Corporate Design für Austausch & Neuerrichtung von Heizungs- und Klimatechnik
Zielgruppe
Austausch, Neuerrichtung modernster Heizungstechnik und Klimatechnik
Unsere Zielgruppe sind Privatpersonen die Ihr Haus zukunftsorientiert beheizen bzw. kühlen wollen
Aufgabenstellung
schlicht, modern, klar
gerne schwarzer Hintergrund und max 3 Farben gerne auch kräftig / auffällig
Nur eine Idee: Vielleicht können kleine Icons im Logo erscheinen.... z.b. 4 Elemente.... Feuer, Wasser, Luft, Erde plus schneeflocke für die klimatechnik (?)

```html
<!DOCTYPE html>
<html lang="de">
<head>
<meta charset="utf-8">
<title>Wärmeraum 7 – Corporate Design</title>
<link href="https://fonts.googleapis.com/css2?family=Signika:wght@300;400;600&display=swap" rel="stylesheet">
<style>
  :root {
    --brand-red: #e30613;
    --brand-grey: #9d9d9d;
    --ink: #1a1a1a;
    --black: #000;
    --paper: #fff;
  }
  * { margin: 0; padding: 0; box-sizing: border-box; }
  html, body { width: 896px; height: 1200px; overflow: hidden; background: var(--paper); }
  body { position: relative; font-family: "Signika", sans-serif; color: var(--ink); }

  .brand-mark { display: flex; align-items: center; }
  .brand-mark__square { background: var(--brand-grey); flex: none; }
  .brand-mark__text { display: flex; flex-direction: column; }
  .brand-mark__name { color: var(--brand-red); font-weight: 400; line-height: 1; }
  .tagline { color: var(--brand-grey); font-weight: 300; line-height: 1.1; }

  /* Hero banner */
  .hero {
    position: absolute; left: 22px; top: 17px; width: 850px; height: 451px;
    background: radial-gradient(ellipse 55% 50% at 50% 50%, #2b2b2b 0%, #141414 55%, var(--black) 100%);
    display: flex; align-items: center; justify-content: center;
  }
  .hero .brand-mark__square { width: 90px; height: 90px; margin-right: 34px; }
  .hero .brand-mark__name { font-size: 64px; }
  .hero .tagline { font-size: 27px; margin-top: 4px; }

  /* Business cards */
  .card { position: absolute; left: 38px; width: 312px; height: 192px; box-shadow: 2px 4px 8px rgba(0,0,0,.35); overflow: hidden; }
  .card--front { top: 620px; background: var(--black); display: flex; flex-direction: column; align-items: center; justify-content: center; }
  .card--front .brand-mark { flex-direction: column; }
  .card--front .brand-mark__square { width: 46px; height: 46px; margin-bottom: 16px; }
  .card--front .brand-mark__name { font-size: 34px; text-align: center; }
  .card--front .tagline { font-size: 14px; text-align: center; margin-top: 2px; }

  .card--back { top: 880px; background: var(--paper); display: flex; }
  .card--back .card__logo-area { width: 128px; display: flex; align-items: center; justify-content: center; }
  .card--back .brand-mark__square { width: 50px; height: 50px; }
  .card__contact { width: 152px; background: var(--brand-red); color: var(--paper); text-align: center; padding-top: 30px; font-size: 10.5px; line-height: 1.3; }
  .card__company, .card__person { font-weight: 600; font-size: 11.5px; }
  .card__role { font-size: 11.5px; font-weight: 300; margin-bottom: 20px; }
  .card__address { font-size: 10px; }
  .card__contact svg { width: 7px; height: 7px; vertical-align: -1px; margin-right: 2px; fill: var(--paper); }

  /* Letterhead */
  .letterhead { position: absolute; left: 419px; top: 533px; width: 438px; height: 619px; background: var(--paper); box-shadow: 3px 4px 10px rgba(0,0,0,.35); }
  .letterhead__band { height: 7px; background: var(--brand-red); }
  .letterhead .brand-mark { position: absolute; left: 133px; top: 28px; }
  .letterhead .brand-mark__square { width: 28px; height: 28px; margin-right: 12px; }
  .letterhead .brand-mark__name { font-size: 21px; }
  .letterhead .tagline { font-size: 9px; }
  .letterhead__sender { position: absolute; left: 73px; top: 102px; font-size: 4.4px; letter-spacing: -0.02em; }
  .letterhead__info { position: absolute; left: 321px; top: 104px; font-size: 6.4px; font-weight: 300; line-height: 1.25; }
  .letterhead__info p + p { margin-top: 8px; }
  .letterhead__info svg { width: 6px; height: 6px; vertical-align: -1px; margin-right: 1px; fill: var(--ink); }
  .fold-mark { position: absolute; left: 0; height: 0.6px; background: #bbb; }
  .letterhead__footer { position: absolute; left: 0; top: 576px; width: 100%; height: 29px; background: var(--black); color: var(--paper); font-size: 6.2px; font-weight: 400; padding: 6px 0 0 46px; line-height: 1.35; }
  .letterhead__tax { position: absolute; left: 292px; top: 6px; }
</style>
</head>
<body>

<section class="hero">
  <div class="brand-mark">
    <span class="brand-mark__square"></span>
    <div class="brand-mark__text">
      <span class="brand-mark__name">Wärmeraum 7</span>
      <span class="tagline">heizen. kühlen. wohlfühlen.</span>
    </div>
  </div>
</section>

<article class="card card--front">
  <div class="brand-mark">
    <span class="brand-mark__square"></span>
    <div class="brand-mark__text">
      <span class="brand-mark__name">Wärmeraum 7</span>
      <span class="tagline">heizen. kühlen. wohlfühlen.</span>
    </div>
  </div>
</article>

<article class="card card--back">
  <div class="card__logo-area brand-mark"><span class="brand-mark__square"></span></div>
  <div class="card__contact">
    <p class="card__company">Wärmeraum7</p>
    <p class="card__person">Max Mustermann</p>
    <p class="card__role">Geschäftsführer</p>
    <p class="card__address">Musterstraße 12<br>12345 Musterstadt</p>
    <p class="card__address"><svg viewBox="0 0 10 10"><rect x="2" y="0" width="6" height="10" rx="1"/></svg>+49 123 123 123 123</p>
    <p class="card__address">@ info@waermeraum7.com</p>
    <p class="card__address"><svg viewBox="0 0 10 10"><circle cx="5" cy="5" r="5"/></svg>www.waermeraum7.com</p>
  </div>
</article>

<article class="letterhead">
  <div class="letterhead__band"></div>
  <div class="brand-mark">
    <span class="brand-mark__square"></span>
    <div class="brand-mark__text">
      <span class="brand-mark__name">Wärmeraum 7</span>
      <span class="tagline">heizen. kühlen. wohlfühlen.</span>
    </div>
  </div>
  <p class="letterhead__sender">Max Mustermann · Musterstraße 123 · 12345 Musterstadt</p>
  <div class="letterhead__info">
    <p>Max Mustermann<br>Geschäftsführer</p>
    <p>Musterweg 10<br>12345 Musterstadt<br>
      <svg viewBox="0 0 10 10"><path d="M2 0l2 2-1 2q1 2 3 3l2-1 2 2-2 2Q3 10 0 2z"/></svg>+049 123 123 123<br>
      @ info@waermeraum7.de<br>
      <svg viewBox="0 0 10 10"><circle cx="5" cy="5" r="4.5"/></svg>www.waermeraum7.de</p>
  </div>
  <span class="fold-mark" style="top:219px;width:16px"></span>
  <span class="fold-mark" style="top:310px;left:10px;width:10px"></span>
  <span class="fold-mark" style="top:438px;width:16px"></span>
  <footer class="letterhead__footer">
    <p>Regionalbank Musterhausen eG<br>IBAN: DE 12 1234 1234 1234 1234 12 • BIC: ABCDEFGHIJK</p>
    <p class="letterhead__tax">U-St.-Nr. 000 000 000</p>
  </footer>
</article>

</body>
</html>
```